New Business Cards for NYC Salon

We are updating all of our cards. 7142-2869-4057 is my account number. We put names of our stylists on their cards. The back should include appointment space. Were looking for something more sleek and modern. Black/White Silver... or even touches of the orange color on our website which has been our thing for years. The design should communicate professional upscale boutique salon for men and women. Should be able to incorporate design into thank you cards, referral cards, brochure and postcards. The file is a zip file...we like the stacked ones black or white or the side versions.

Industry/Entity Type

Beauty Salon

Contact Information for Business Card

Marcus John's Salon313 W. 53rd Street, New York NY 10019 212-386-7714 info@marcusdellsalon.example www.marcusdellsalon.example

Font styles to use
Other font styles liked:
• trajan

Requirements
Must have
• we print a different card for every person in the salon. Begin by designing with the name Marcus. We will change it with every employee when printing. Must have a space for appointment date and time.
Nice to have
• Were looking to move towards the stacked or side placed logo but not opposed to utilizing the circular.
Should not have
• Photos

```html
<!DOCTYPE html>
<html lang="en">
<head>
<meta charset="utf-8">
<title>Marcus Dell's Salon – Business Card</title>
<link rel="stylesheet" href="https://fonts.googleapis.com/css2?family=PT+Sans:ital,wght@0,400;0,700;1,400;1,700&display=swap">
<style>
  :root {
    --canvas-bg: #e6e6e8;
    --card-black: #050505;
    --card-white: #fbfbfb;
    --ink-dark: #111111;
    --ink-light: #ffffff;
    --rule-light: #9a9a9a;
    --card-shadow: rgba(0, 0, 0, 0.22);
  }
  * { box-sizing: border-box; margin: 0; padding: 0; }
  html, body {
    width: 1200px;
    height: 864px;
    overflow: hidden;
  }
  body {
    background: var(--canvas-bg);
    font-family: "PT Sans", sans-serif;
    position: relative;
  }
  .card {
    position: absolute;
    top: 277px;
    width: 540px;
    height: 309px;
    border-radius: 3px;
    box-shadow: 0 6px 18px var(--card-shadow);
  }

  /* Appointment (back) side */
  .card--appointment {
    left: 40px;
    background: var(--card-black);
    color: var(--ink-light);
  }
  .appointment__title {
    position: absolute;
    top: 34px;
    left: 0;
    width: 100%;
    text-align: center;
    font-weight: 700;
    font-size: 22px;
  }
  .appointment__row {
    position: absolute;
    left: 58px;
    right: 52px;
    display: flex;
    align-items: flex-end;
    font-size: 15px;
  }
  .appointment__row--name { top: 88px; }
  .appointment__row--date { top: 124px; }
  .appointment__row--time { top: 160px; }
  .appointment__label { white-space: nowrap; margin-right: 14px; }
  .appointment__line {
    flex: 1;
    border-bottom: 1px solid var(--rule-light);
    margin-bottom: 4px;
  }
  .appointment__meridiem { margin: 0 14px 0 8px; position: relative; top: 12px; }
  .appointment__meridiem:last-child { margin-right: 0; }
  .appointment__note {
    position: absolute;
    top: 228px;
    left: 0;
    width: 100%;
    text-align: center;
    font-style: italic;
    font-weight: 700;
    font-size: 15px;
  }

  /* Contact (front) side */
  .card--contact {
    left: 620px;
    background: var(--card-white);
    color: var(--ink-dark);
  }
  .brand-mark {
    position: absolute;
    top: 48px;
    right: 48px;
    display: flex;
    align-items: center;
    gap: 10px;
    font-size: 15px;
    letter-spacing: 0.22em;
    text-transform: uppercase;
  }
  .brand-mark__square {
    width: 14px;
    height: 14px;
    background: var(--ink-dark);
  }
  .card__name {
    position: absolute;
    top: 108px;
    left: 34px;
    font-weight: 700;
    font-size: 22px;
  }
  .contact-list {
    position: absolute;
    right: 30px;
    bottom: 30px;
    list-style: none;
    text-align: right;
    font-size: 15.5px;
    line-height: 1.5;
  }
  .contact-list__item {
    display: flex;
    justify-content: flex-end;
    align-items: center;
    gap: 10px;
  }
  .contact-list__icon {
    width: 17px;
    height: 17px;
    border-radius: 3px;
    background: var(--ink-dark);
    display: inline-flex;
    align-items: center;
    justify-content: center;
  }
  .contact-list__icon svg { width: 11px; height: 11px; }
</style>
</head>
<body>

<section class="card card--appointment" aria-label="Appointment side">
  <h2 class="appointment__title">Your Next Appointment is</h2>
  <div class="appointment__row appointment__row--name">
    <span class="appointment__label">Name :</span><span class="appointment__line"></span>
  </div>
  <div class="appointment__row appointment__row--date">
    <span class="appointment__label">Date :</span><span class="appointment__line"></span>
  </div>
  <div class="appointment__row appointment__row--time">
    <span class="appointment__label">Time:</span>
    <span class="appointment__line"></span><span class="appointment__meridiem">AM</span>
    <span class="appointment__line"></span><span class="appointment__meridiem">PM</span>
  </div>
  <p class="appointment__note">If unable to keep appointment, kindly give 24hrs notice.</p>
</section>

<section class="card card--contact" aria-label="Contact side">
  <div class="brand-mark">
    <span class="brand-mark__square"></span>
    <span class="brand-mark__name">Marcus Dell's Salon</span>
  </div>
  <h1 class="card__name">Marcus Dell's Salon</h1>
  <ul class="contact-list">
    <li class="contact-list__item">212-386-7714
      <span class="contact-list__icon"><svg viewBox="0 0 12 12"><path d="M2.5 1h2l1 3-1.3 1a6 6 0 0 0 2.8 2.8L8 6.5l3 1v2A1.5 1.5 0 0 1 9.5 11 8.5 8.5 0 0 1 1 2.5 1.5 1.5 0 0 1 2.5 1z" fill="#fff"/></svg></span>
    </li>
    <li class="contact-list__item">info@marcusdellsalon.example
      <span class="contact-list__icon"><svg viewBox="0 0 12 12"><rect x="1" y="2.5" width="10" height="7" fill="none" stroke="#fff" stroke-width="1.2"/><path d="M1 2.5l5 4 5-4" fill="none" stroke="#fff" stroke-width="1.2"/></svg></span>
    </li>
    <li class="contact-list__item">marcusdellsalon.example
      <span class="contact-list__icon"><svg viewBox="0 0 12 12"><path d="M5 7l2-2M4.5 5.5l-2 2a1.6 1.6 0 0 0 2 2l2-2M7.5 6.5l2-2a1.6 1.6 0 0 0-2-2l-2 2" fill="none" stroke="#fff" stroke-width="1.3" stroke-linecap="round"/></svg></span>
    </li>
    <li class="contact-list__item">748 E. 29th Street, New York NY 10016
      <span class="contact-list__icon"><svg viewBox="0 0 12 12"><path d="M6 11.5S2 7.2 2 4.6a4 4 0 0 1 8 0C10 7.2 6 11.5 6 11.5z" fill="#fff"/><circle cx="6" cy="4.6" r="1.4" fill="#111"/></svg></span>
    </li>
  </ul>
</section>

</body>
</html>
```